Brightwell Giving Inc

We need a full re-design of our non-profit organization website (www.brightwellgiving.org). Ideally, we are looking to make it more attractive, user-friendly, and interactive with our business model.

Please make sure to user colors that ago with our logo.

We need a homepage done and we also need a content page done where we will use for the other pages to fill with content.

Target Market(s)

Clothes/textiles donations.

Industry/Entity Type

Charity

Number of Pages Required

2 page

Colors

Designer to choose colors to be used in the design.

Requirements
Must have
• It must match the styling of our logo and same colors as current website. (www.brightwellgiving.org)
Nice to have
• Sleek homepage that is easy to understand and get our main points across.

```html
<!DOCTYPE html>
<html lang="en">
<head>
<meta charset="utf-8">
<title>Brightwell Giving – Home</title>
<link href="https://fonts.googleapis.com/css2?family=Oswald:wght@400;500;600;700&family=Open+Sans:wght@400;600;700&display=swap" rel="stylesheet">
<style>
:root{
  --green:#3d6b1e;
  --green-dark:#2e5414;
  --yellow:#f2c300;
  --yellow-deep:#e6b400;
  --ink:#1e1e1e;
  --text:#555;
  --muted:#8a8a8a;
  --light:#f2f2f2;
  --white:#fff;
  --footer:#1c1c1c;
}
*{margin:0;padding:0;box-sizing:border-box}
html,body{width:1200px;height:5099px;overflow:hidden}
body{font-family:"Open Sans",Arial,sans-serif;color:var(--text);background:var(--white);position:relative}
.heading{font-family:"Oswald",Arial,sans-serif;text-transform:uppercase;color:var(--ink)}
.section{position:absolute;left:0;width:1200px}
.btn{display:inline-block;font-family:"Oswald",Arial,sans-serif;font-size:13px;letter-spacing:1px;text-transform:uppercase;padding:9px 26px;background:var(--yellow);color:var(--ink)}
.btn-green{background:var(--green);color:var(--white)}
.divider{display:block;margin:10px auto 0;width:160px;height:16px}

/* header */
.site-header{position:absolute;top:0;left:0;width:1200px;height:74px;z-index:3;display:flex;align-items:center;padding:0 80px;background:rgba(0,0,0,.55);white-space:nowrap}
.brand{display:flex;align-items:center;gap:8px;font-family:"Oswald",Arial,sans-serif;font-size:19px;font-weight:600;color:var(--yellow);text-transform:uppercase;margin-right:34px}
.brand-mark{width:20px;height:20px;background:var(--yellow)}
.main-nav{display:flex;gap:16px;font-family:"Oswald",Arial,sans-serif;font-size:11px;color:var(--white);text-transform:uppercase;letter-spacing:.5px}
.main-nav .active{color:var(--yellow)}
.header-contact{margin-left:auto;display:flex;gap:20px;color:var(--white);font-size:10px}
.header-contact div{display:flex;align-items:center;gap:6px}
.header-contact b{display:block;color:var(--yellow);font-size:11px}

/* hero */
.hero{top:0;height:570px}
.hero-photo{position:absolute;inset:0;background:linear-gradient(180deg,#5a4632 0%,#7b5a3b 45%,#3a2a1d 100%)}
.hero-content{position:absolute;top:330px;width:100%;text-align:center}
.hero-title{font-family:"Oswald",Arial,sans-serif;font-size:56px;font-weight:700;color:var(--white);text-transform:uppercase;line-height:1}
.hero-title span{color:var(--yellow)}
.hero-sub{font-family:"Oswald",Arial,sans-serif;font-size:30px;color:var(--white);margin:6px 0 18px}

/* about */
.about{top:570px;height:560px}
.about-text{position:absolute;left:148px;top:120px;width:430px}
.about-text h2{font-size:34px;color:var(--green);font-weight:600}
.about-text h3{font-family:"Oswald",Arial,sans-serif;font-size:20px;color:var(--yellow-deep);text-transform:uppercase;letter-spacing:1px}
.about-text .lead{font-size:17px;color:#444;margin:14px 0 16px;line-height:1.45}
.about-text p{font-size:12px;line-height:1.75;margin-bottom:18px}
.about-frame-green{position:absolute;left:620px;top:66px;width:390px;height:390px;background:var(--green);border-radius:56px 8px 56px 8px}
.about-frame-yellow{position:absolute;left:612px;top:80px;width:385px;height:390px;background:var(--yellow);border-radius:8px 56px 8px 56px}
.about-photo{position:absolute;left:628px;top:82px;width:355px;height:360px;background:linear-gradient(160deg,#cfc4b4,#8d7b66);border-radius:10px 50px 10px 50px}

/* how it works */
.how{top:1080px;height:570px}
.how svg.band{position:absolute;inset:0}
.how-title{position:absolute;top:130px;width:100%;text-align:center;color:var(--white);font-size:34px;font-weight:600}
.steps{position:absolute;top:240px;left:150px;width:900px;display:flex;justify-content:space-between}
.step{width:270px;text-align:center;color:var(--white)}
.step-icon{width:86px;height:86px;border-radius:50%;background:var(--white);margin:0 auto 18px;display:flex;align-items:center;justify-content:center}
.step h4{font-family:"Oswald",Arial,sans-serif;font-size:14px;text-transform:uppercase;margin-bottom:8px}
.step p{font-size:11px;line-height:1.6;opacity:.9}
.step .more{display:block;margin-top:8px;font-family:"Oswald",Arial,sans-serif;font-size:11px;text-transform:uppercase}

/* recipients */
.recipients{top:1650px;height:730px;text-align:center}
.recipients h2{font-size:34px;color:var(--green);font-weight:600}
.recipients .tagline{font-family:"Oswald",Arial,sans-serif;font-size:17px;color:#333;letter-spacing:1px}
.levels{display:flex;gap:30px;justify-content:center;margin-top:34px}
.level{width:235px;height:440px;background:var(--white);box-shadow:0 3px 14px rgba(0,0,0,.16);position:relative}
.level-head{height:70px;background:var(--ink);color:var(--white);font-family:"Oswald",Arial,sans-serif;font-size:30px;display:flex;align-items:center;justify-content:center;clip-path:polygon(0 0,100% 0,100% 80%,50% 100%,0 80%)}
.price{font-family:"Oswald",Arial,sans-serif;color:var(--yellow-deep);font-size:46px;font-weight:600;line-height:1;margin:26px 0 20px;height:70px;display:flex;flex-direction:column;justify-content:center}
.price small{font-size:26px;color:var(--ink)}
.level ul{list-style:none;padding:0 16px;font-size:10px;color:#444}
.level li{padding:12px 0;border-bottom:1px solid #e6e6e6}
.level .btn{position:absolute;bottom:28px;left:50%;transform:translateX(-50%);font-size:12px;padding:7px 20px}
.recipients .see-more{margin-top:54px}

/* gallery */
.gallery{top:2320px;height:650px}
.gallery svg.band{position:absolute;inset:0}
.photo-frame{position:absolute;border:6px solid var(--white);box-shadow:0 4px 14px rgba(0,0,0,.25)}
.photo-fill{width:100%;height:100%}

/* news */
.news{top:2975px;height:700px;text-align:center}
.news h2{font-size:34px;font-weight:600;color:var(--ink)}
.news-card{position:absolute;background:var(--light);text-align:left}
.news-card h4{font-family:"Oswald",Arial,sans-serif;font-size:22px;text-transform:uppercase;color:var(--ink);line-height:1.15;padding:14px 14px 4px}
.news-card .date{font-size:9px;color:var(--muted);padding:0 14px}
.news-card p{font-size:10px;line-height:1.6;padding:6px 14px}
.news-card .more{font-size:9px;padding:6px 14px 14px;color:#444;text-transform:uppercase}
.news-photo{width:100%}

/* testimonials */
.testimonials{top:3690px;height:510px;background:#f6f6f6;text-align:center}
.testimonials h2{font-size:34px;font-weight:600;padding-top:44px}
.quotes{display:grid;grid-template-columns:repeat(3,325px);gap:22px 18px;justify-content:center;margin-top:38px}
.quote{background:var(--white);height:130px;box-shadow:0 2px 8px rgba(0,0,0,.08);display:flex;flex-direction:column;align-items:center;justify-content:center;gap:14px}
.quote .mark{font-family:Georgia,serif;font-size:66px;line-height:.5;height:30px;font-weight:700}
.quote .mark.green{color:var(--green)}
.quote .mark.dark{color:var(--ink)}
.quote p{font-family:"Oswald",Arial,sans-serif;font-size:12px;text-transform:uppercase;color:#333;letter-spacing:.5px}

/* map + finder */
.map{top:4200px;height:410px;background:linear-gradient(180deg,#cfe0ea 0%,#e7e3d6 60%,#d9e6cf 100%)}
.finder{top:4610px;height:100px;background:var(--yellow);display:flex;align-items:center;padding:0 150px}
.finder h3{font-size:26px;font-weight:600}
.finder-search{margin-left:auto;width:500px;height:40px;background:var(--white);display:flex;align-items:center;padding:0 14px;font-size:12px;color:var(--muted);justify-content:space-between}

/* footer */
.site-footer{top:4710px;height:389px;background:var(--footer);color:#bdbdbd}
.footer-cols{display:flex;gap:40px;padding:50px 150px 0}
.footer-col h5{font-family:"Oswald",Arial,sans-serif;color:var(--white);font-size:15px;text-transform:uppercase;margin-bottom:14px;font-weight:500}
.footer-col p,.footer-col li{font-size:10px;line-height:1.7}
.footer-col ul{list-style:none}
.footer-col li::before{content:"› ";color:var(--yellow)}
.badges{display:flex;gap:6px;margin:14px 0 10px}
.badges span{width:32px;height:36px;background:var(--yellow)}
.social{display:flex;gap:6px}
.social span{width:20px;height:20px;background:#3a3a3a}
.field{width:200px;height:24px;border:1px solid #444;background:#2a2a2a;margin-bottom:8px;font-size:9px;padding:5px 8px;color:#888}
.field.tall{height:60px}
.footer-bottom{position:absolute;bottom:0;left:0;width:100%;height:44px;border-top:1px solid #333;display:flex;align-items:center;padding:0 150px;font-size:10px;color:#888}
</style>
</head>
<body>

<header class="site-header">
  <div class="brand"><span class="brand-mark"></span>Brightwell Giving</div>
  <nav class="main-nav">
    <span class="active">Home</span><span>Services ▾</span><span>Charity ▾</span><span>How it works</span><span>About us</span><span>Locations</span><span>News</span><span>Donate</span><span>Wall of fame</span>
  </nav>
  <div class="header-contact">
    <div><svg width="14" height="14" viewBox="0 0 24 24"><path fill="#f2c300" d="M6.6 10.8a15 15 0 0 0 6.6 6.6l2.2-2.2c.3-.3.7-.4 1-.2 1.1.4 2.3.6 3.6.6.6 0 1 .4 1 1V20c0 .6-.4 1-1 1A17 17 0 0 1 3 4c0-.6.4-1 1-1h3.5c.6 0 1 .4 1 1 0 1.3.2 2.5.6 3.6.1.3 0 .7-.2 1z"/></svg><span>Main line<b>555-014-2210</b></span></div>
    <div><svg width="14" height="14" viewBox="0 0 24 24"><path fill="#f2c300" d="M6.6 10.8a15 15 0 0 0 6.6 6.6l2.2-2.2c.3-.3.7-.4 1-.2 1.1.4 2.3.6 3.6.6.6 0 1 .4 1 1V20c0 .6-.4 1-1 1A17 17 0 0 1 3 4c0-.6.4-1 1-1h3.5c.6 0 1 .4 1 1 0 1.3.2 2.5.6 3.6.1.3 0 .7-.2 1z"/></svg><span>Toll free<b>555-019-8834</b></span></div>
  </div>
</header>

<section class="section hero">
  <div class="hero-photo" role="img" aria-label="Smiling children gathered together outdoors"></div>
  <div class="hero-content">
    <h1 class="hero-title">Welcome to Brightwell <span>Giving</span></h1>
    <p class="hero-sub">Think globally while donating locally</p>
    <span class="btn">Read more</span>
  </div>
</section>

<section class="section about">
  <div class="about-text">
    <h2 class="heading">About us</h2>
    <h3>Brightwell Giving</h3>
    <p class="lead">We are a family based non-profit organization in the name of Brightwell Giving Inc</p>
    <p>We started this foundation to give back to the community and make it easier for every household to pass on the clothing and shoes they no longer need. Each donation is sorted, reused or recycled so that nothing goes to waste. Since we began, we have proudly donated to many local families, shelters and community groups that are already helping our neighbourhoods grow stronger.</p>
    <span class="btn">Read more</span>
  </div>
  <div class="about-frame-green"></div>
  <div class="about-frame-yellow"></div>
  <div class="about-photo" role="img" aria-label="Volunteers serving food at a community event"></div>
</section>

<section class="section how">
  <svg class="band" width="1200" height="570" viewBox="0 0 1200 570" preserveAspectRatio="none" aria-hidden="true">
    <path d="M0 40 C250 -10 450 90 700 40 C900 0 1050 30 1200 10 L1200 520 C1000 560 800 500 600 540 C400 575 200 520 0 545 Z" fill="#3d6b1e"/>
  </svg>
  <h2 class="heading how-title">How it works</h2>
  <svg class="divider" style="position:absolute;top:190px;left:520px" viewBox="0 0 160 16" aria-hidden="true"><line x1="0" y1="8" x2="68" y2="8" stroke="#fff"/><line x1="92" y1="8" x2="160" y2="8" stroke="#fff"/><path d="M80 14 L72 7 a4 4 0 0 1 8-3 a4 4 0 0 1 8 3 Z" fill="none" stroke="#fff"/></svg>
  <div class="steps">
    <div class="step">
      <div class="step-icon"><svg width="44" height="44" viewBox="0 0 44 44"><path d="M22 10 a4 4 0 1 1 4 4 L22 18 L6 30 H38 L22 18" fill="none" stroke="#3d6b1e" stroke-width="3"/></svg></div>
      <h4>Drop off clothing at your closest donation bin</h4>
      <p>We have bins placed across many neighbourhoods. Find the one nearest to you and drop off clean clothing, shoes and household textiles at any time.</p>
      <span class="more">Read more »</span>
    </div>
    <div class="step">
      <div class="step-icon"><svg width="48" height="44" viewBox="0 0 48 44"><path d="M4 14 H30 V30 H4 Z M30 19 H39 L44 25 V30 H30" fill="none" stroke="#3d6b1e" stroke-width="3"/><circle cx="12" cy="33" r="4" fill="#3d6b1e"/><circle cx="36" cy="33" r="4" fill="#3d6b1e"/></svg></div>
      <h4>We pick it up and take it to our sorting facility</h4>
      <p>Our team collects the bins on a regular route and brings the items to our sorting facility, where everything is checked and grouped by type.</p>
      <span class="more">Read more »</span>
    </div>
    <div class="step">
      <div class="step-icon"><svg width="44" height="44" viewBox="0 0 44 44"><path d="M8 26 C14 22 20 24 24 27 H32 C34 27 34 31 32 31 H22 M24 31 L36 26 C39 25 40 29 38 30 L26 37 H8" fill="none" stroke="#3d6b1e" stroke-width="3"/><circle cx="24" cy="12" r="5" fill="none" stroke="#3d6b1e" stroke-width="3"/></svg></div>
      <h4>Charities get clothing, we pay you for the clothes</h4>
      <p>Sorted clothing goes to partner charities and families in need, and the proceeds help fund programs that support our local community.</p>
      <span class="more">Read more »</span>
    </div>
  </div>
</section>

<section class="section recipients" style="padding-top:40px">
  <h2 class="heading">Donation recipients</h2>
  <p class="tagline">Think Globally while Donating Locally</p>
  <div class="levels">
    <div class="level">
      <div class="level-head">LEVEL 1</div>
      <div class="price">$1000</div>
      <ul><li>Brightwell Giving youth sports program</li><li>Brightwell Giving school supplies drive</li><li>Brightwell Giving winter coat campaign</li><li>Brightwell Giving local food pantry support</li></ul>
      <span class="btn btn-green">Donate</span>
    </div>
    <div class="level">
      <div class="level-head">LEVEL 2</div>
      <div class="price">$1000-<small>$2500</small></div>
      <ul><li>Brightwell Giving donation to community shelters</li><li>Brightwell Giving donation to family relief fund</li><li>Donation made to neighbourhood outreach services</li></ul>
      <span class="btn btn-green">Donate</span>
    </div>
    <div class="level">
      <div class="level-head">LEVEL 3</div>
      <div class="price">$2500-<small>$5000</small></div>
      <ul><li>Brightwell Giving donation to disaster recovery</li></ul>
      <span class="btn btn-green">Donate</span>
    </div>
    <div class="level">
      <div class="level-head">LEVEL 4</div>
      <div class="price">$5000-<small>$10000</small></div>
      <ul><li>Community development grant for regional organizations</li><li>Phase 1 – regional children's health partner program</li></ul>
      <span class="btn btn-green">Donate</span>
    </div>
  </div>
  <span class="btn see-more">See more</span>
</section>

<section class="section gallery">
  <svg class="band" width="1200" height="650" viewBox="0 0 1200 650" preserveAspectRatio="none" aria-hidden="true">
    <path d="M0 60 C300 0 600 40 900 20 C1050 10 1150 0 1200 10 L1200 600 C900 640 600 580 300 620 C150 640 60 620 0 630 Z" fill="#f2c300"/>
  </svg>
  <div class="photo-frame" style="left:95px;top:100px;width:490px;height:375px"><div class="photo-fill" role="img" aria-label="Staff member beside a green donation bin on a trailer" style="background:linear-gradient(160deg,#9aa6a8,#4f7a3a 60%,#5d5d5d)"></div></div>
  <div class="photo-frame" style="left:612px;top:100px;width:485px;height:180px"><div class="photo-fill" role="img" aria-label="Green donation bins at a parking lot" style="background:linear-gradient(160deg,#b9c2c7,#3f8a4a 60%,#6b6b6b)"></div></div>
  <div class="photo-frame" style="left:612px;top:292px;width:485px;height:183px"><div class="photo-fill" role="img" aria-label="Team members holding a banner at an event" style="background:linear-gradient(160deg,#c9c9c9,#9b8d7c 60%,#4c4c4c)"></div></div>
</section>

<section class="section news" style="padding-top:30px">
  <h2 class="heading">Latest news</h2>
  <svg class="divider" viewBox="0 0 160 16" aria-hidden="true"><line x1="0" y1="8" x2="68" y2="8" stroke="#999"/><line x1="92" y1="8" x2="160" y2="8" stroke="#999"/><path d="M80 14 L72 7 a4 4 0 0 1 8-3 a4 4 0 0 1 8 3 Z" fill="none" stroke="#999"/></svg>
  <div class="news-card" style="left:153px;top:125px;width:300px;height:530px">
    <div class="news-photo" role="img" aria-label="Staff member next to a donation bin" style="height:265px;background:linear-gradient(160deg,#a8b4b8,#3f8a4a 60%,#555)"></div>
    <h4>Brightwell Giving Online Store</h4>
    <div class="date">05 March 2018</div>
    <p>We opened our online store so supporters can shop gently used clothing from home. Every purchase helps fund local programs and keeps good textiles in use for longer. Visit the store and discover new items added each week.</p>
    <div class="more">» Read more</div>
  </div>
  <div class="news-card" style="left:470px;top:105px;width:285px;height:400px">
    <div class="news-photo" role="img" aria-label="Ribbon cutting in front of a thrift store" style="height:220px;background:linear-gradient(160deg,#7d8fa0,#b7a58a 60%,#6f5b4a)"></div>
    <h4>Brightwell Giving Street Sales</h4>
    <div class="date">12 April 2018</div>
    <p>Our spring street sales drew a great crowd. Thank you to every volunteer and shopper who helped raise funds for families in our area.</p>
    <div class="more">» Read more</div>
  </div>
  <div class="news-card" style="left:770px;top:105px;width:285px;height:560px">
    <h4 style="padding-top:24px">Charity Project Love Thy Neighbor-Elena</h4>
    <div class="date">20 March 2018</div>
    <p>A local family received clothing, household goods and support through our neighbour project. We are grateful to every donor who made this possible and helped them make a fresh start this season.</p>
    <div class="more">» Read more</div>
    <div role="img" aria-label="Group of people standing in a circle on a lawn" style="position:absolute;left:0;bottom:0;width:100%;height:250px;background:linear-gradient(160deg,#8cb06a,#4f7f36)"></div>
  </div>
</section>

<section class="section testimonials">
  <h2 class="heading">Testimonials</h2>
  <div class="quotes">
    <div class="quote"><span class="mark dark">“</span><p>We are an open book organization</p></div>
    <div class="quote"><span class="mark green">“</span><p>We are a true 501(c)(3) non profit organization</p></div>
    <div class="quote"><span class="mark dark">“</span><p>Our goal is to be with and within the community</p></div>
    <div class="quote"><span class="mark dark">“</span><p>Support anti gun violence</p></div>
    <div class="quote"><span class="mark green">“</span><p>Help disaster victims of Hurricane Irene</p></div>
    <div class="quote"><span class="mark dark">“</span><p>Help Riverbend family &amp; youth council</p></div>
  </div>
</section>

<section class="section map" role="img" aria-label="Regional map marking donation bin locations"></section>

<section class="section finder">
  <h3 class="heading">Find local donation place</h3>
  <div class="finder-search"><span>Zip</span><svg width="16" height="16" viewBox="0 0 24 24"><circle cx="10" cy="10" r="6" fill="none" stroke="#888" stroke-width="2"/><line x1="15" y1="15" x2="21" y2="21" stroke="#888" stroke-width="2"/></svg></div>
</section>

<footer class="section site-footer">
  <div class="footer-cols">
    <div class="footer-col" style="width:260px">
      <h5>Brightwell Giving</h5>
      <p>Brightwell Giving is a non-profit organization that was created for one purpose: helping the local community through clothing donations. We collect, sort and share textiles with families and partners across the region.</p>
      <div class="badges"><span></span><span></span><span></span><span></span></div>
      <div class="social"><span></span><span></span><span></span><span></span><span></span><span></span></div>
    </div>
    <div class="footer-col" style="width:170px">
      <h5>Information</h5>
      <p>Main office<br>48 Orchard Lane, Suite 2<br>Millbrook, NY 10000<br><br>Warehouse<br>112 Depot Road<br>Millbrook, NY 10001<br><br>Store<br>9 Market Street<br>Millbrook, NY 10002</p>
    </div>
    <div class="footer-col" style="width:150px">
      <h5>Quik link</h5>
      <ul><li>Home</li><li>Services</li><li>Charity</li><li>How it works</li><li>About us</li><li>Locations</li><li>News</li><li>Donate</li><li>Wall of fame</li></ul>
    </div>
    <div class="footer-col">
      <h5>Contact us</h5>
      <div class="field">Name</div>
      <div class="field">Email</div>
      <div class="field tall">Message</div>
      <span class="btn" style="padding:5px 18px;font-size:11px">Send</span>
    </div>
  </div>
  <div class="footer-bottom">© 2018 Brightwell Giving. All rights reserved.</div>
</footer>

</body>
</html>
```